VC Pitch Deck Design

We have all the content, we just need a designer to add the magic graphic touch!

WOULD PREFER IT DO BE DONE IN KEYNOTE!!!

Target Market(s)

Investor Pitch Deck

we want it to be like a story ... yes we started with a coffee ordering App and we started here ... and now we are here doing this etc.

Industry/Entity Type

Vc

Font styles to use
Sans Serif

Colors
00a990

```html
<!DOCTYPE html>
<html lang="en">
<head>
<meta charset="utf-8">
<title>DailyBrew – Smart Ordering</title>
<link rel="stylesheet" href="https://fonts.googleapis.com/css2?family=Roboto+Condensed:wght@100;200;300;400&display=swap">
<style>
  :root {
    --teal: #00b99b;
    --teal-deep: #00a388;
    --white: #ffffff;
    --night: #1e2455;
    --dusk: #5a4f7c;
    --glow: #c6a489;
  }
  * { margin: 0; padding: 0; box-sizing: border-box; }
  html, body {
    width: 1200px;
    height: 900px;
    overflow: hidden;
    background: var(--teal);
  }
  .slide {
    position: relative;
    width: 1200px;
    height: 900px;
    background: var(--teal);
    font-family: "Roboto Condensed", "Arial Narrow", sans-serif;
    color: var(--white);
  }
  .headline-band {
    position: absolute;
    top: 0; left: 0;
    width: 1200px;
    height: 114px;
    display: flex;
    align-items: center;
    justify-content: center;
    padding-left: 48px;
  }
  .teaser {
    font-weight: 300;
    font-size: 46px;
    line-height: 1;
    white-space: nowrap;
    margin-top: 4px;
  }
  .mood-visual {
    position: absolute;
    top: 114px; left: 0;
    width: 1200px;
    height: 444px;
    background: linear-gradient(90deg, var(--glow) 0%, var(--dusk) 28%, var(--night) 50%, var(--dusk) 72%, var(--glow) 100%);
  }
  .statement-band {
    position: absolute;
    top: 558px; left: 0;
    width: 1200px;
    height: 279px;
    display: flex;
    align-items: center;
    justify-content: center;
    padding-left: 82px;
  }
  .statement {
    font-weight: 200;
    font-size: 195px;
    line-height: 1;
    margin-top: -16px;
    transform: scaleX(0.89);
    white-space: nowrap;
  }
  .footer {
    position: absolute;
    bottom: 0; left: 0;
    width: 1200px;
    height: 63px;
    background: var(--teal-deep);
    display: flex;
    align-items: center;
    justify-content: flex-end;
    padding-right: 22px;
    font-size: 22px;
  }
  .brand-name { font-weight: 300; font-size: 26px; }
  .tagline { font-weight: 300; margin-left: 6px; }
</style>
</head>
<body>
  <main class="slide">
    <header class="headline-band">
      <p class="teaser">{YAWN} Here we go another coffee ordering App…</p>
    </header>
    <div class="mood-visual" role="img" aria-label="Photograph of mirrored blurred bokeh city lights in cream, peach, pink and green on a deep navy background"></div>
    <section class="statement-band">
      <h1 class="statement">WRONG!</h1>
    </section>
    <footer class="footer">
      <span class="brand-name">DailyBrew</span>
      <span class="tagline">- smart ordering</span>
    </footer>
  </main>
</body>
</html>
```